Website Design for BRAVO FREIGHTWAY

Hello. We are a Freight Brokage business in the transportation and logistics industry in the USA. Company name is BRAVO FREIGHTWAY. I'm looking to have a 5 page or less website built. Must have HOME, SHIPPERS, CARRIERS, ABOUT and CONTACT US.. I have additional information that needs to be placed in the footer of the website. Company address, contact info privacy and terms and conditions Need nice, vibrant looking site. The website needs to be a fully functionable site that is built and coded for wordpress and ready for hosting. Please visit these link for you to have an idea of the look and feel I want. www.tolvanhaulage.example www.corvel-transit.example. Will have logo concept in 2 days for upload. As time goes by I will supply more content and the layout of the respective pages.

```html
<!DOCTYPE html>
<html lang="en">
<head>
<meta charset="utf-8">
<title>Bravo Freightway</title>
<link href="https://fonts.googleapis.com/css2?family=Fira+Sans:wght@500;600;700&family=Poppins:ital,wght@0,400;0,500;0,600;1,400&display=swap" rel="stylesheet">
<style>
:root{
  --green:#0a9b4c;
  --green-dark:#087a3c;
  --ink:#111;
  --nav:#10181f;
  --grey-bg:#f4f4f4;
  --text:#444;
  --white:#fff;
  --dark-panel:#3b3d40;
}
*{box-sizing:border-box;margin:0;padding:0}
html,body{width:1200px;height:3871px;overflow:hidden}
body{font-family:"Poppins",sans-serif;color:var(--text);background:var(--white);position:relative}
.abs{position:absolute}
.heading{font-family:"Fira Sans",sans-serif;font-weight:600;color:var(--ink)}
.accent{color:var(--green)}
.body-copy{font-size:9.8px;letter-spacing:-.25px;line-height:20px}
.btn{position:absolute;display:flex;align-items:center;justify-content:center;font-family:"Poppins",sans-serif;font-weight:600;font-size:11px;letter-spacing:.3px;text-transform:uppercase;border-radius:3px}
.btn-solid{background:var(--green);color:var(--white)}
.btn-outline{border:2px solid var(--green);color:var(--green);background:var(--white)}
.bar{position:absolute;height:4px;width:38px;background:var(--green);left:50%;margin-left:-19px}
.section-title{position:absolute;left:0;width:1200px;text-align:center;font-size:31px}

/* nav */
.site-nav{position:absolute;top:0;left:0;width:1200px;height:62px;background:var(--nav)}
.brand{position:absolute;left:164px;top:17px;font-family:"Fira Sans",sans-serif;font-weight:700;font-size:22px;color:var(--green);letter-spacing:.3px}
.nav-links{position:absolute;top:24px;left:512px;display:flex;font-size:10.5px;font-weight:600;color:var(--white)}
.nav-links span{margin-right:26px}
/* hero */
.hero{position:absolute;top:62px;left:0;width:1200px;height:561px}
.hero-photo{position:absolute;inset:0;background:linear-gradient(180deg,#6f6a8a 0%,#b88a8a 28%,#c79a7f 45%,#5e5552 70%,#2b2a2c 100%)}
.hero-title{position:absolute;left:164px;top:124px;font-family:"Fira Sans",sans-serif;font-weight:700;font-size:62px;line-height:64px;color:var(--white)}
.hero-text{position:absolute;left:164px;top:276px;width:450px;font-size:11px;letter-spacing:-.2px;line-height:21px;color:var(--white)}
.dots{position:absolute;top:531px;left:582px;display:flex;gap:4px}
.dots i{width:7px;height:7px;border-radius:50%;background:#bbb;display:block}
.dots i:first-child{background:var(--white)}
/* about */
.about-photo{position:absolute;left:162px;top:689px;width:491px;height:364px;border:4px solid var(--green);background:linear-gradient(160deg,#d78a3a 0%,#c06a2a 40%,#6d6f78 70%,#9a9ca3 100%)}
.about-card{position:absolute;left:584px;top:722px;width:454px;height:296px;background:var(--white);box-shadow:0 6px 24px rgba(0,0,0,.16)}
.about-card h2{position:absolute;left:32px;top:34px;font-size:30px}
.about-card p{position:absolute;left:32px;top:94px;width:396px;text-align:justify}
/* services */
.services{position:absolute;top:1129px;left:0;width:1200px;height:531px;background:var(--grey-bg)}
.service{position:absolute;top:128px;width:275px;text-align:center}
.service .ph{height:188px}
.service h3{margin-top:16px;font-family:"Poppins",sans-serif;font-weight:600;font-size:13.5px;color:#222}
.service p{margin-top:8px;padding:0 14px}
.service .btn{position:relative;width:135px;height:33px;margin:14px auto 0}
/* split */
.split{position:absolute;top:1660px;width:600px;height:339px;text-align:center;color:var(--white)}
.split .bg{position:absolute;inset:0}
.split h2{position:absolute;left:0;width:600px;top:44px;font-family:"Fira Sans",sans-serif;font-weight:600;font-size:41px;color:var(--white)}
.split .line{position:absolute;top:104px;left:281px;width:38px;height:4px;background:var(--white)}
.split p{position:absolute;left:104px;top:118px;width:392px;text-align:justify;text-align-last:center}
.split .btn{top:252px;left:232px;width:136px;height:33px}
/* why */
.why{position:absolute;top:1999px;left:0;width:1200px;height:608px;background:var(--grey-bg)}
.why-item h4{font-family:"Poppins",sans-serif;font-weight:600;font-size:14px;color:var(--green)}
.why-item p{font-size:10px;letter-spacing:-.2px;line-height:19px;margin-top:6px}
.why-left{text-align:right;width:200px}
.why-right{text-align:left;width:200px}
.why-center{position:absolute;left:0;width:1190px;text-align:center;font-family:"Fira Sans",sans-serif;font-weight:600;font-size:34px;line-height:46px}
/* testimonials */
.testi{position:absolute;top:2741px;width:238px;height:302px;background:var(--grey-bg);text-align:center}
.testi.featured{background:var(--white);box-shadow:0 6px 22px rgba(0,0,0,.15)}
.avatar{width:80px;height:80px;border-radius:50%;margin:29px auto 0;background:linear-gradient(180deg,#8a7d6f,#4e5a66)}
.testi p{margin-top:22px;padding:0 16px;font-style:italic;font-size:9.8px;letter-spacing:-.2px;line-height:20.5px;text-align:justify;text-align-last:center;color:#555}
.testi .who{margin-top:10px;font-weight:600;font-size:13px;color:var(--green)}
/* contact */
.contact{position:absolute;top:3121px;left:0;width:1200px;height:434px}
.contact-bg{position:absolute;inset:0;background:linear-gradient(90deg,#128a44 0%,#17a154 45%,#1aa85a 100%)}
.contact h2{position:absolute;left:0;width:1200px;top:58px;text-align:center;font-size:31px;color:var(--white)}
.info{position:absolute;left:243px;color:var(--white);font-size:11px;line-height:21px;display:flex;gap:14px}
.info svg{flex:none;margin-top:2px}
.field{position:absolute;background:var(--white);font-size:10px;color:#777;padding:8px 9px}
.contact .btn{border:2px solid var(--white);color:var(--white);background:transparent;left:557px;top:334px;width:135px;height:33px}
/* footer */
.footer{position:absolute;top:3555px;left:0;width:1200px;height:316px;background:#0e0e0e;color:var(--white)}
.f-logo{position:absolute;left:140px;width:200px;text-align:center;font-family:"Fira Sans",sans-serif;font-weight:700;font-size:28px;color:var(--green);line-height:40px}
.social{position:absolute;top:163px;left:180px;display:flex;gap:12px}
.social i{display:block;width:22px;height:22px;border:2px solid var(--green);border-radius:50%}
.f-col{position:absolute;top:60px;font-size:10px;line-height:22.5px}
.f-col h5{font-family:"Poppins",sans-serif;font-weight:600;font-size:11px;margin-bottom:11px;letter-spacing:.3px}
.f-contact{display:flex;gap:9px;line-height:16px;margin-bottom:9px}
.f-input{width:164px;height:30px;border:1px solid #ccc;background:var(--white);border-radius:3px;font-size:9.5px;color:#888;padding:8px 12px;margin-top:8px}
.f-sub{width:164px;height:30px;background:var(--green);border-radius:3px;margin-top:9px;display:flex;align-items:center;justify-content:center;font-weight:600;font-size:9.5px}
.f-rule{position:absolute;top:236px;left:132px;width:936px;height:1px;background:#555}
.copy{position:absolute;top:256px;left:0;width:1200px;text-align:center;font-size:10.5px}
</style>
</head>
<body>

<header class="site-nav">
  <div class="brand">BRAVO FREIGHTWAY</div>
  <nav class="nav-links"><span>HOME</span><span>SHIPPERS</span><span>CARRIERS</span><span>ABOUT</span><span>CONTACT US</span></nav>
  <div class="btn btn-solid" style="left:901px;top:15px;width:135px;height:32px">Request a quote</div>
</header>

<section class="hero">
  <div class="hero-photo" role="img" aria-label="Semi truck driving on a desert highway at sunset"></div>
  <h1 class="hero-title">Welcome To<br>Bravo Freightway</h1>
  <p class="hero-text">Lorem ipsum dolor sit amet, consectetur adipiscing elit, sed do eiusmod tempor incididunt ut labore et dolore magna aliqua.</p>
  <div class="btn btn-solid" style="left:164px;top:335px;width:135px;height:33px">Get started</div>
  <div class="dots"><i></i><i></i><i></i><i></i></div>
</section>

<section class="about">
  <div class="about-photo" role="img" aria-label="Truck with trailer parked below an orange sunlit mountain"></div>
  <div class="about-card">
    <h2 class="heading">About <span class="accent">Bravo Freightway</span></h2>
    <p class="body-copy">Lorem ipsum dolor sit amet, consectetur adipiscing elit, sed do eiusmod tempor incididunt ut labore et dolore magna aliqua. Quis ipsum suspendisse ultrices gravida. Risus commodo viverra maecenas accumsan lacus vel facilisis. perspiciatis unde omnis iste natus error sit voluptatem accusantium doloremque laudantium, totam rem aperiam, eaque ipsa quae ab illo inventore veritatis et quasi architecto beatae vitae dicta sunt explicabo.</p>
    <div class="btn btn-solid" style="left:32px;top:226px;width:135px;height:34px">Learn more</div>
  </div>
</section>

<section class="services">
  <h2 class="section-title heading" style="top:64px">Our <span class="accent">Services</span></h2>
  <div class="bar" style="top:107px"></div>
  <div class="service" style="left:162px">
    <div class="ph" role="img" aria-label="Forklift moving a wrapped pallet in a warehouse" style="background:linear-gradient(160deg,#5d7a9a,#c65a2a 70%,#d0d0d0)"></div>
    <h3>LOREM IPSUM DOLOR SIT</h3>
    <p class="body-copy">Lorem ipsum dolor sit amet, consectetur adipiscing elit, sed do eiusmod tempor incididunt ut labore et dolore magna aliqua.</p>
    <div class="btn btn-outline">Learn more</div>
  </div>
  <div class="service" style="left:463px">
    <div class="ph" role="img" aria-label="Row of closed loading dock doors" style="background:linear-gradient(180deg,#7a7d82,#b7babd 60%,#8c8e90)"></div>
    <h3>LOREM IPSUM DOLOR SIT</h3>
    <p class="body-copy">Lorem ipsum dolor sit amet, consectetur adipiscing elit, sed do eiusmod tempor incididunt ut labore et dolore magna aliqua.</p>
    <div class="btn btn-outline">Learn more</div>
  </div>
  <div class="service" style="left:763px">
    <div class="ph" role="img" aria-label="Two truck drivers standing in front of a red truck" style="background:linear-gradient(160deg,#8a2a2a,#5a5f66 50%,#2f3a4e)"></div>
    <h3>LOREM IPSUM DOLOR SIT</h3>
    <p class="body-copy">Lorem ipsum dolor sit amet, consectetur adipiscing elit, sed do eiusmod tempor incididunt ut labore et dolore magna aliqua.</p>
    <div class="btn btn-outline">Learn more</div>
  </div>
</section>

<section class="split" style="left:0">
  <div class="bg" role="img" aria-label="Warehouse loading docks under a dark overlay" style="background:linear-gradient(180deg,#45474a,#35373a)"></div>
  <h2>Shippers</h2><div class="line"></div>
  <p class="body-copy">Lorem ipsum dolor sit amet, consectetur adipiscing elit, sed do eiusmod tempor incididunt ut labore et dolore magna aliqua. Quis ipsum suspendisse ultrices gravida. Risus commodo viverra maecenas accumsan lacus vel facilisis. perspiciatis unde omnis iste natus error sit voluptatem accusantium doloremque laudantium, totam rem aperiam, eaque ipsa quae ab illo inventore veritatis et quasi architecto beatae vitae dicta sunt explicabo.</p>
  <div class="btn btn-solid">Learn more</div>
</section>
<section class="split" style="left:600px">
  <div class="bg" role="img" aria-label="Truck trailer under a green overlay" style="background:linear-gradient(180deg,#0c9e4e,#0a944a)"></div>
  <h2>Carriers</h2><div class="line"></div>
  <p class="body-copy">Lorem ipsum dolor sit amet, consectetur adipiscing elit, sed do eiusmod tempor incididunt ut labore et dolore magna aliqua. Quis ipsum suspendisse ultrices gravida. Risus commodo viverra maecenas accumsan lacus vel facilisis. perspiciatis unde omnis iste natus error sit voluptatem accusantium doloremque laudantium, totam rem aperiam, eaque ipsa quae ab illo inventore veritatis et quasi architecto beatae vitae dicta sunt explicabo.</p>
  <div class="btn" style="background:#2d2d2d;color:#fff">Learn more</div>
</section>

<section class="why">
  <h2 class="section-title heading" style="top:70px">Why <span class="accent">Choose Us ?</span></h2>
  <div class="bar" style="top:112px"></div>
  <svg class="abs" style="left:0;top:0" width="1200" height="608" viewBox="0 0 1200 608">
    <defs>
      <g id="trolley" fill="none" stroke="#fff" stroke-width="1.6" stroke-linecap="round" stroke-linejoin="round">
        <path d="M-9 -10 L-5 -10 L-1 8 L10 6"/>
        <rect x="-1" y="-9" width="8" height="6" transform="rotate(-12)"/>
        <rect x="0" y="-2" width="9" height="6" transform="rotate(-12)"/>
        <circle cx="-1" cy="10" r="2"/>
      </g>
    </defs>
    <path d="M476 155 A160 160 0 1 0 712 155" fill="none" stroke="#0a9b4c" stroke-width="2.5"/>
    <circle cx="476" cy="155" r="4" fill="#0a9b4c"/>
    <circle cx="712" cy="155" r="4" fill="#0a9b4c"/>
    <g fill="#0a9b4c" stroke="#f4f4f4" stroke-width="3">
      <circle cx="451" cy="200" r="27"/><circle cx="739" cy="200" r="27"/>
      <circle cx="463" cy="340" r="27"/><circle cx="731" cy="340" r="27"/>
      <circle cx="593" cy="422" r="27"/>
    </g>
    <use href="#trolley" x="451" y="200"/><use href="#trolley" x="739" y="200"/>
    <use href="#trolley" x="463" y="340"/><use href="#trolley" x="731" y="340"/>
    <use href="#trolley" x="593" y="422"/>
  </svg>
  <div class="why-center" style="top:222px"><span class="accent">BRAVO</span><br>FREIGHTWAY</div>
  <div class="abs why-item why-left" style="left:214px;top:166px"><h4>Lorem ipsum dolor</h4><p>Lorem ipsum dolor sit amet, consectetur adipiscing elit sed do.</p></div>
  <div class="abs why-item why-right" style="left:786px;top:166px"><h4>Lorem ipsum dolor</h4><p>Lorem ipsum dolor sit amet, consectetur adipiscing elit sed do.</p></div>
  <div class="abs why-item why-left" style="left:214px;top:306px"><h4>Lorem ipsum dolor</h4><p>Lorem ipsum dolor sit amet, consectetur adipiscing elit sed do.</p></div>
  <div class="abs why-item why-right" style="left:779px;top:306px"><h4>Lorem ipsum dolor</h4><p>Lorem ipsum dolor sit amet, consectetur adipiscing elit sed do.</p></div>
  <div class="abs why-item" style="left:493px;top:462px;width:200px;text-align:center"><h4>Lorem ipsum dolor</h4><p>Lorem ipsum dolor sit amet, consectetur adipiscing elit sed do.</p></div>
</section>

<section class="testimonials">
  <h2 class="section-title heading" style="top:2662px">Our <span class="accent">Client Testimonials</span></h2>
  <div class="bar" style="top:2705px"></div>
  <div class="testi" style="left:207px">
    <div class="avatar" role="img" aria-label="Client portrait"></div>
    <p>Lorem ipsum dolor sit amet, consectetur adipiscing elit, sed do eiusmod tempor incididunt ut labore et dolore magna aliqua. Quis ipsum suspendisse ultrices gravida. Risus commodo viverra maecenas accumsan lacus vel facilisis.</p>
    <div class="who">- John Smith</div>
  </div>
  <div class="testi featured" style="left:482px">
    <div class="avatar" role="img" aria-label="Client portrait"></div>
    <p>Lorem ipsum dolor sit amet, consectetur adipiscing elit, sed do eiusmod tempor incididunt ut labore et dolore magna aliqua. Quis ipsum suspendisse ultrices gravida. Risus commodo viverra maecenas accumsan lacus vel facilisis.</p>
    <div class="who">- John Smith</div>
  </div>
  <div class="testi" style="left:757px">
    <div class="avatar" role="img" aria-label="Client portrait"></div>
    <p>Lorem ipsum dolor sit amet, consectetur adipiscing elit, sed do eiusmod tempor incididunt ut labore et dolore magna aliqua. Quis ipsum suspendisse ultrices gravida. Risus commodo viverra maecenas accumsan lacus vel facilisis.</p>
    <div class="who">- John Smith</div>
  </div>
</section>

<section class="contact">
  <div class="contact-bg" role="img" aria-label="Semi truck in a yard under a green overlay"></div>
  <h2 class="heading">Get In Touch</h2>
  <div class="info" style="top:176px">
    <svg width="20" height="22" viewBox="0 0 20 22"><path d="M10 1a7 7 0 0 0-7 7c0 5 7 13 7 13s7-8 7-13a7 7 0 0 0-7-7z" fill="#fff"/><circle cx="10" cy="8" r="2.6" fill="#17a154"/></svg>
    <span>123 Lorem ipsum dolor sit amet, con-<br>sectetur adipiscing.</span>
  </div>
  <div class="info" style="top:238px">
    <svg width="20" height="20" viewBox="0 0 20 20"><path d="M4 1l4 1 1 5-2.5 1.5a11 11 0 0 0 5 5L13 11l5 1 1 4-3 3C8 19 1 12 1 4z" fill="#fff"/></svg>
    <span>+1 888 888 8888</span>
  </div>
  <div class="info" style="top:283px">
    <svg width="20" height="20" viewBox="0 0 20 20"><rect x="1" y="4" width="18" height="13" fill="#fff"/><path d="M1 4l9 7 9-7" fill="none" stroke="#17a154" stroke-width="1.6"/></svg>
    <span>info@bravofreightway.example</span>
  </div>
  <div class="info" style="top:329px">
    <svg width="20" height="20" viewBox="0 0 20 20" fill="none" stroke="#fff" stroke-width="1.6"><circle cx="10" cy="10" r="8.5"/><ellipse cx="10" cy="10" rx="3.5" ry="8.5"/><path d="M1.5 10h17M3 6h14M3 14h14"/></svg>
    <span>www.bravofreightway.example</span>
  </div>
  <div class="field" style="left:557px;top:158px;width:197px;height:31px">First Name</div>
  <div class="field" style="left:759px;top:158px;width:198px;height:31px">Last Name</div>
  <div class="field" style="left:557px;top:200px;width:197px;height:31px">Email:</div>
  <div class="field" style="left:759px;top:200px;width:198px;height:31px">Phone:</div>
  <div class="field" style="left:557px;top:239px;width:400px;height:69px">Message:</div>
  <div class="btn">Submit now</div>
</section>

<footer class="footer">
  <div class="f-logo" style="top:72px">BRAVO<br>FREIGHTWAY</div>
  <div class="social"><i></i><i></i><i></i><i></i></div>
  <div class="f-col" style="left:372px"><h5>NAVIGATION</h5>Home<br>Shippers<br>Carriers<br>About<br>Contact Us</div>
  <div class="f-col" style="left:497px"><h5>OUR SERVICES</h5>Lorem ipsum dolor<br>Sit amet consectetur<br>Adipiscing elit, sed do<br>Eiusmod tempor inci</div>
  <div class="f-col" style="left:649px;width:190px">
    <h5>CONTACT US</h5>
    <div class="f-contact"><svg width="12" height="14" viewBox="0 0 20 22"><path d="M10 1a7 7 0 0 0-7 7c0 5 7 13 7 13s7-8 7-13a7 7 0 0 0-7-7z" fill="#0a9b4c"/></svg><span>123 Lorem ipsum dolor sit amet,<br>consectetur</span></div>
    <div class="f-contact"><svg width="12" height="12" viewBox="0 0 20 20"><path d="M4 1l4 1 1 5-2.5 1.5a11 11 0 0 0 5 5L13 11l5 1 1 4-3 3C8 19 1 12 1 4z" fill="#0a9b4c"/></svg><span>Call Us:<br>+1 888 888 8888</span></div>
    <div class="f-contact"><svg width="12" height="12" viewBox="0 0 20 20"><rect x="1" y="4" width="18" height="13" fill="#0a9b4c"/><path d="M1 4l9 7 9-7" fill="none" stroke="#0e0e0e" stroke-width="1.6"/></svg><span>Email Address:<br>info@bravofreightway.example</span></div>
  </div>
  <div class="f-col" style="left:865px"><h5>SIGN UP EMAIL</h5><div style="line-height:14px">Sign up for our email list</div><div class="f-input">Email address</div><div class="f-sub">SUBSCRIBE NOW</div></div>
  <div class="f-rule"></div>
  <div class="copy">© copyrights 2022 <span class="accent">BRAVO FREIGHTWAY</span> &nbsp;|&nbsp;&nbsp; All rights reserved.</div>
</footer>

</body>
</html>
```